Weightloss company needs Business Card

We want a business card that is clean and professional, yet portrays that we are a friendly, innovative, and versatile program designed to fit the needs of our clients.
I would like there to be 2 sides, one side having an appointment card, and the other side containing the logo and business information. There can be decorations on both sides. The logo is attached.

Target Market(s)

Men and women 40-60

Industry/Entity Type

Business

Contact Information for Business Card

Font styles to use
Sans Serif

Requirements
Must have
• The logo, space for business information
Nice to have
• The colors in the logo
Should not have
• No pictures of people or food

```html
<!DOCTYPE html>
<html lang="en">
<head>
<meta charset="utf-8">
<title>Turnpoint Wellness Business Card</title>
<link rel="stylesheet" href="https://fonts.googleapis.com/css2?family=Source+Sans+3:ital,wght@0,400;0,600;1,400&display=swap">
<style>
  :root {
    --sky: #55c8ec;
    --red: #ed1c3a;
    --ink: #231f20;
    --grey: #9a9a9a;
    --paper: #ffffff;
    --backdrop: #e9e6e3;
  }
  html, body {
    margin: 0;
    width: 1200px;
    height: 1200px;
    overflow: hidden;
    background: var(--backdrop);
    font-family: "Source Sans 3", sans-serif;
  }
  .card {
    position: absolute;
    left: 200px;
    width: 801px;
    height: 454px;
    background: var(--paper);
    box-shadow: 0 3px 8px rgba(0,0,0,0.25);
    overflow: hidden;
  }
  .card--front { top: 102px; }
  .card--back { top: 644px; }
  .card__art {
    position: absolute;
    inset: 0;
    width: 100%;
    height: 100%;
  }
  .txt {
    position: absolute;
    margin: 0;
    line-height: 1;
    white-space: nowrap;
  }
  /* front */
  .person__name { left: 48px; top: 158px; font-size: 31px; color: var(--red); }
  .person__role { left: 48px; top: 191px; font-size: 21px; color: var(--ink); }
  .contact { left: 48px; font-size: 21px; color: var(--ink); display: flex; align-items: center; gap: 18px; }
  .contact svg { width: 20px; height: 20px; flex: none; }
  .contact--phone { top: 230px; }
  .contact--mail { top: 257px; }
  .contact--web { top: 284px; }
  .address { left: 48px; top: 334px; font-size: 21px; color: var(--ink); line-height: 28px; }
  .brand-name {
    right: 86px; top: 104px;
    font-size: 40px; font-weight: 600; color: var(--red);
    text-align: right; line-height: 36px;
  }
  /* back */
  .appt__title { left: 62px; top: 59px; font-size: 32px; color: var(--sky); letter-spacing: 0.5px; }
  .appt__label { font-size: 21px; color: var(--sky); }
  .appt__day { font-size: 21px; color: var(--grey); }
  .rule { position: absolute; height: 0; border-top: 1.5px solid #6d6d6d; }
  .appt__note {
    position: absolute; left: 65px; top: 309px; width: 457px;
    margin: 0; font-size: 18.5px; font-style: italic; color: var(--sky);
    line-height: 23px; text-align: justify;
  }
</style>
</head>
<body>

<section class="card card--front" aria-label="Business card front">
  <svg class="card__art" viewBox="0 0 1001 568" preserveAspectRatio="none" aria-hidden="true">
    <rect width="1001" height="568" fill="var(--sky)"/>
    <path d="M357,0 C357,270 600,490 895,568 C620,470 430,250 415,0 Z" fill="var(--red)"/>
    <path d="M415,0 C430,250 620,470 895,568 L1001,568 L1001,0 Z" fill="var(--paper)"/>
  </svg>

  <p class="txt brand-name">Turnpoint<br>Wellness</p>

  <p class="txt person__name">Dana Merrow</p>
  <p class="txt person__role">Managing Partner</p>

  <p class="txt contact contact--phone">
    <svg viewBox="0 0 20 20" aria-hidden="true"><path d="M2 7 C2 3 18 3 18 7 L18 9 L14 9 L14 7 C12 6 8 6 6 7 L6 9 L2 9 Z" fill="var(--red)"/><path d="M5 10 L15 10 L17 17 L3 17 Z" fill="var(--red)"/><circle cx="10" cy="13.5" r="2" fill="var(--sky)"/></svg>
    555.014.2270
  </p>
  <p class="txt contact contact--mail">
    <svg viewBox="0 0 20 20" aria-hidden="true"><rect x="1" y="4" width="18" height="12" fill="var(--red)"/><path d="M1.5 4.5 L10 11 L18.5 4.5 M1.5 15.5 L7.5 9.5 M18.5 15.5 L12.5 9.5" stroke="var(--sky)" stroke-width="1.3" fill="none"/></svg>
    hello@turnpointwell.net
  </p>
  <p class="txt contact contact--web">
    <svg viewBox="0 0 20 20" aria-hidden="true"><circle cx="10" cy="10" r="9" fill="var(--red)"/><g stroke="var(--sky)" stroke-width="1" fill="none"><ellipse cx="10" cy="10" rx="4" ry="9"/><path d="M1 10 H19 M2.5 5.5 H17.5 M2.5 14.5 H17.5 M10 1 V19"/></g></svg>
    www.turnpointwell.net
  </p>

  <p class="txt address">2150 Alder Lane<br>Marlow Falls, WA 98012</p>
</section>

<section class="card card--back" aria-label="Appointment card back">
  <svg class="card__art" viewBox="0 0 1001 568" preserveAspectRatio="none" aria-hidden="true">
    <rect width="1001" height="568" fill="var(--sky)"/>
    <rect width="650" height="568" fill="var(--paper)"/>
    <circle cx="650" cy="335" r="335" fill="var(--paper)"/>
  </svg>

  <p class="txt appt__title">APPOINMENT</p>

  <p class="txt appt__label" style="left:62px; top:132px;">For</p>
  <div class="rule" style="left:122px; top:149px; width:392px;"></div>
  <p class="txt appt__label" style="left:62px; top:170px;">With</p>
  <div class="rule" style="left:122px; top:187px; width:392px;"></div>

  <p class="txt appt__label" style="left:62px; top:209px;">On:</p>
  <p class="txt appt__day" style="left:122px; top:209px;">Mon.</p>
  <p class="txt appt__day" style="left:192px; top:209px;">Tues.</p>
  <p class="txt appt__day" style="left:265px; top:209px;">Wed.</p>
  <p class="txt appt__day" style="left:341px; top:209px;">Thurs.</p>
  <p class="txt appt__day" style="left:426px; top:209px;">Fri.</p>
  <p class="txt appt__day" style="left:482px; top:209px;">Sat.</p>

  <div class="rule" style="left:62px; top:268px; width:202px;"></div>
  <p class="txt appt__label" style="left:276px; top:253px;">at</p>
  <div class="rule" style="left:300px; top:268px; width:131px;"></div>
  <p class="txt appt__label" style="left:446px; top:253px;">AM/PM</p>

  <p class="appt__note">This time is reserved for you. If you are unable to keep your appointment, please let us know at least 24 hours in advance so that we may be schedule a time for you. Thank you for your consideration.</p>
</section>

</body>
</html>
```